Eye catching Stationary Design

Healthcare consultant firm looking for stationary design ( letterhead, envelope and business cards) That’s professional, classy and eye catching . The design should incorporate the logo and the colors of the logo in its design. You can see the logo on our website at www harbor key advisors. com.

```html
<!DOCTYPE html>
<html lang="en">
<head>
<meta charset="utf-8">
<title>Harbor Key Advisors – Stationery</title>
<link href="https://fonts.googleapis.com/css2?family=Marcellus+SC&family=Lato:wght@400;700&display=swap" rel="stylesheet">
<style>
  :root{
    --bg:#e6e8e9;
    --paper:#ffffff;
    --sky:#2a9fd6;
    --navy:#1f4f9c;
    --ink:#2a3550;
    --muted:#6b7688;
    --folder:#dcedf9;
  }
  *{box-sizing:border-box;margin:0;padding:0}
  html,body{width:1200px;height:1000px;overflow:hidden}
  body{background:var(--bg);position:relative;font-family:"Lato",sans-serif;color:var(--ink)}
  .sheet{position:absolute;background:var(--paper);box-shadow:0 6px 18px rgba(0,0,0,.12);overflow:hidden}
  .swoosh{position:absolute;left:0;width:100%}
  .brand{font-family:"Marcellus SC",serif;color:var(--navy);letter-spacing:.5px;white-space:nowrap}

  /* Letterhead */
  .letterhead{left:390px;top:60px;width:380px;height:520px}
  .letterhead .swoosh-top{top:0;height:40px}
  .letterhead .swoosh-bottom{bottom:0;height:40px}
  .letterhead .brand{position:absolute;top:50px;width:100%;text-align:center;font-size:15px}
  .letterhead .contact-row{position:absolute;bottom:52px;left:22px;right:22px;display:flex;justify-content:space-between;font-size:7.5px;color:var(--muted)}
  .icon{display:inline-block;width:8px;height:8px;border-radius:50%;background:var(--navy);vertical-align:middle;margin-right:3px}

  /* Folder */
  .folder{left:800px;top:100px;width:360px;height:500px;background:var(--folder)}
  .folder .brand{position:absolute;top:240px;width:100%;text-align:center;font-size:18px}

  /* Envelope */
  .envelope{left:320px;top:640px;width:500px;height:240px}
  .envelope .wedge{position:absolute;top:0;height:100%;width:40px}
  .envelope .wedge-left{left:0}
  .envelope .wedge-right{right:0}
  .envelope .sender{position:absolute;left:54px;top:34px}
  .envelope .brand{font-size:14px;margin-bottom:10px}
  .contact-list{list-style:none;font-size:7.5px;color:var(--muted);line-height:1.8}

  /* Business cards */
  .card{width:250px;height:145px;left:50px}
  .card-back{top:360px}
  .card-back .wedge{position:absolute;top:0;height:100%;width:22px}
  .card-back .wedge-left{left:0}
  .card-back .wedge-right{right:0}
  .card-back .content{position:absolute;left:36px;top:20px}
  .card-back .brand{font-size:11px;margin-bottom:10px}
  .card-back .person{font-size:8.5px;font-weight:700;letter-spacing:.5px}
  .card-back .role{font-size:6.5px;color:var(--muted);margin-bottom:8px}
  .card-back .contact-list{font-size:6.5px;line-height:1.6}
  .card-front{top:530px}
  .card-front .band{position:absolute;left:0;width:100%;height:28px;background:var(--navy)}
  .card-front .band-top{top:0}
  .card-front .band-bottom{bottom:0}
  .card-front .brand{position:absolute;top:64px;width:100%;text-align:center;font-size:12px}
</style>
</head>
<body>

<section class="sheet letterhead" aria-label="Letterhead">
  <svg class="swoosh swoosh-top" viewBox="0 0 380 40" preserveAspectRatio="none">
    <path d="M70 0 Q190 30 320 0 L330 0 Q190 40 60 0Z" fill="var(--sky)"/>
  </svg>
  <div class="brand">Harbor Key Advisors LLC</div>
  <div class="contact-row">
    <span><i class="icon"></i>118 Maple Row Suite 4, Portland, OR 97205, USA</span>
    <span><i class="icon"></i>(503) 555-0148</span>
    <span><i class="icon"></i>info@harborkeyadvisors.com</span>
  </div>
  <svg class="swoosh swoosh-bottom" viewBox="0 0 380 40" preserveAspectRatio="none">
    <path d="M60 40 Q190 0 330 40 L320 40 Q190 10 70 40Z" fill="var(--sky)"/>
  </svg>
</section>

<section class="sheet folder" aria-label="Presentation folder">
  <div class="brand">Harbor Key Advisors LLC</div>
</section>

<section class="sheet envelope" aria-label="Envelope">
  <svg class="wedge wedge-left" viewBox="0 0 40 240" preserveAspectRatio="none"><path d="M0 0 L40 0 L0 240Z" fill="var(--sky)"/></svg>
  <div class="sender">
    <div class="brand">Harbor Key Advisors LLC</div>
    <ul class="contact-list">
      <li><i class="icon"></i>118 Maple Row Suite 4, Portland, OR 97205, USA</li>
      <li><i class="icon"></i>(503) 555-0148</li>
      <li><i class="icon"></i>info@harborkeyadvisors.com</li>
    </ul>
  </div>
  <svg class="wedge wedge-right" viewBox="0 0 40 240" preserveAspectRatio="none"><path d="M40 0 L40 240 L0 240Z" fill="var(--sky)"/></svg>
</section>

<section class="sheet card card-back" aria-label="Business card back">
  <svg class="wedge wedge-left" viewBox="0 0 22 145" preserveAspectRatio="none"><path d="M0 0 L22 0 L0 145Z" fill="var(--sky)"/></svg>
  <div class="content">
    <div class="brand">Harbor Key Advisors LLC</div>
    <div class="person">YOUR NAME HERE</div>
    <div class="role">Job Title</div>
    <ul class="contact-list">
      <li>118 Maple Row Suite 4, Portland, OR 97205</li>
      <li>(503) 555-0148</li>
      <li>info@harborkeyadvisors.com</li>
    </ul>
  </div>
  <svg class="wedge wedge-right" viewBox="0 0 22 145" preserveAspectRatio="none"><path d="M22 0 L22 145 L0 145Z" fill="var(--sky)"/></svg>
</section>

<section class="sheet card card-front" aria-label="Business card front">
  <div class="band band-top"></div>
  <div class="brand">Harbor Key Advisors LLC</div>
  <div class="band band-bottom"></div>
</section>

</body>
</html>
```